QM Candle Tube Packaging Design

Website: www.quorelmaren.com
IG: @quorel.maren
Tagline: Elevate Your Ambiance
My brand is a sophisticated brand with luxury candles made of coconut wax. Im looking for an upscale minimalist chic design.
Discover the transformative power of positive energy with Quorel Maren candles. Indulge in true luxury with our specially crafted coconut wax blend that not only ignites captivating scents but also embodies modern elegance and empowering elements.
At Quorel Maren we're committed to delivering a unique and exhilarating aromatic experience to all candle lovers. Each candle is meticulously handcrafted in small batches using luxury fragrance oils exclusively formulated for coconut wax.
Our candles are:
Clean-burning
Paraben-Free
Phthalate-Free
Skin-Safe
Pet-Friendly

```html
<!DOCTYPE html>
<html lang="en">
<head>
<meta charset="utf-8">
<title>Quorel Maren – Candle Tube Label</title>
<link rel="stylesheet" href="https://fonts.googleapis.com/css2?family=Cormorant+Garamond:wght@300;400&family=Montserrat:wght@400;500&family=Sacramento&family=Libre+Baskerville&display=swap">
<style>
  :root {
    --page: #ffffff;
    --cap: #5a5a5b;
    --body: #c5c1bd;
    --body-shade: #b9b5b1;
    --ink: #5b5959;
  }
  html, body {
    margin: 0;
    width: 1200px;
    height: 750px;
    overflow: hidden;
    background: var(--page);
  }
  .canvas {
    position: relative;
    width: 1200px;
    height: 750px;
  }
  .tube-label {
    position: absolute;
    left: 482px;
    top: 85px;
    width: 272px;
    height: 545px;
    background: linear-gradient(90deg, var(--body-shade) 0%, var(--body) 12%, var(--body) 88%, var(--body-shade) 100%);
    border-radius: 4px 4px 3px 3px;
    color: var(--ink);
    text-align: center;
  }
  .tube-cap {
    position: absolute;
    left: 0; top: 0;
    width: 100%;
    height: 131px;
    background: var(--cap);
    border-radius: 4px 4px 0 0;
  }
  .brand {
    position: absolute;
    top: 213px;
    left: 0; width: 100%;
  }
  .brand-name {
    font-family: "Cormorant Garamond", serif;
    font-weight: 300;
    font-size: 25px;
    letter-spacing: 0.3px;
    line-height: 1;
    margin: 0;
  }
  .brand-sub {
    display: flex;
    align-items: center;
    justify-content: center;
    gap: 6px;
    margin-top: 8px;
    font-family: "Montserrat", sans-serif;
    font-size: 7px;
    letter-spacing: 2.4px;
    line-height: 1;
  }
  .brand-sub .rule {
    width: 14px;
    height: 1px;
    background: var(--ink);
  }
  .brand-motto {
    font-family: "Sacramento", cursive;
    font-size: 8px;
    line-height: 1;
    margin-top: 5px;
  }
  .tagline {
    position: absolute;
    top: 318px;
    left: 0; width: 100%;
    font-family: "Sacramento", cursive;
    font-size: 46px;
    line-height: 40px;
    margin: 0;
    font-weight: 400;
  }
  .tagline .line-one { display: block; text-align: left; padding-left: 7px; }
  .tagline .line-two { display: block; text-align: right; padding-right: 6px; }
  .contact {
    position: absolute;
    top: 424px;
    left: 21px;
    width: 235px;
    display: flex;
    justify-content: space-between;
    align-items: center;
    font-family: "Libre Baskerville", serif;
    font-size: 8.5px;
    line-height: 14px;
    white-space: nowrap;
  }
  .contact .divider {
    width: 1px;
    height: 12px;
    background: var(--ink);
  }
  .features {
    position: absolute;
    top: 466px;
    left: 20px;
    display: flex;
    list-style: none;
    margin: 0; padding: 0;
  }
  .feature {
    width: 46px;
    display: flex;
    flex-direction: column;
    align-items: center;
    gap: 5px;
    font-family: "Montserrat", sans-serif;
    font-size: 5.5px;
    line-height: 1;
    white-space: nowrap;
  }
  .feature svg { width: 18px; height: 18px; fill: var(--ink); }
</style>
</head>
<body>
<main class="canvas">
  <section class="tube-label">
    <div class="tube-cap"></div>

    <div class="brand">
      <h1 class="brand-name">QUOREL MAREN</h1>
      <div class="brand-sub"><span class="rule"></span>HANDMADE CANDLES<span class="rule"></span></div>
      <div class="brand-motto">with purpose and love</div>
    </div>

    <h2 class="tagline">
      <span class="line-one">Elevate Your</span>
      <span class="line-two">Ambiance</span>
    </h2>

    <div class="contact">
      <span>IG: @quorel.maren</span>
      <span class="divider"></span>
      <span>www.quorelmaren.com</span>
    </div>

    <ul class="features">
      <li class="feature">
        <svg viewBox="0 0 16 16" aria-hidden="true"><path d="M8 15 L1.6 8.4 A3.8 3.8 0 0 1 8 3.2 A3.8 3.8 0 0 1 14.4 8.4 Z"/></svg>
        Pet-Friendly
      </li>
      <li class="feature">
        <svg viewBox="0 0 16 16" aria-hidden="true"><path d="M8 9 L4.6 5.6 A2 2 0 0 1 8 3 A2 2 0 0 1 11.4 5.6 Z"/><path d="M1 8 Q2 13 8 14 Q14 13 15 8 L13 8 Q12 11 8 12 Q4 11 3 8 Z"/></svg>
        Skin-Safe
      </li>
      <li class="feature">
        <svg viewBox="0 0 16 16" aria-hidden="true"><path d="M11 1 L15 5 L13.5 6.5 L9.5 2.5 Z"/><path d="M9 4 L12 7 L5 14 L3 15 L1 15 L1 13 L2 11 Z"/></svg>
        Phthalate-Free
      </li>
      <li class="feature">
        <svg viewBox="0 0 16 16" aria-hidden="true"><path d="M2 14 Q1 5 9 2 Q9 11 2 14 Z"/><path d="M6 14 Q8 7 15 6 Q14 13 6 14 Z"/></svg>
        Paraben-Free
      </li>
      <li class="feature">
        <svg viewBox="0 0 16 16" aria-hidden="true"><path d="M8 1 Q12 5 11 9 Q10 11 8 11 Q6 11 5.5 9 Q5 6 8 1 Z"/><path d="M1 11 L5 12 L11 12 L15 10 L15 12 L11 15 L1 15 Z"/></svg>
        Clean-burning
      </li>
    </ul>
  </section>
</main>
</body>
</html>
```